Business card for hedge fund
Vornelle Capital Management
Project: Business card for hedge fund
Business card for hedge fund - Financial Services
Creative Brief
Professional
Wanrudee Halvorsen
Chief Operating Officer
wanru.halvorsen@vornellecap.example
2 additional names: Martin Gaskell, Portfolio Manager p: +1-555-382-4719 e-mail: martin.gaskell@vornellecap.example Jia Luo, Portfolio Manager p: +852-5123-9046 e: jia.luo@vornellecap.example No address to be included

```html
<!DOCTYPE html>
<html lang="en">
<head>
<meta charset="utf-8">
<title>Vornelle Capital Management – Business Card</title>
<link rel="stylesheet" href="https://fonts.googleapis.com/css2?family=Cinzel:wght@400;500&family=Open+Sans:ital,wght@0,400;0,600;0,700;1,400&display=swap">
<style>
  :root {
    --backdrop: #e9eaec;
    --card-white: #ffffff;
    --panel-dark: #4a4b4d;
    --panel-darker: #38393b;
    --accent-orange: #f39a1e;
    --accent-yellow: #f7c548;
    --ink-dark: #2f3033;
    --ink-light: #f2f2f2;
    --ink-muted: #c9c9c9;
    --faint-grey: #dcdddf;
  }
  * { box-sizing: border-box; margin: 0; padding: 0; }
  html, body { width: 1200px; height: 998px; overflow: hidden; }
  body {
    background: var(--backdrop);
    font-family: "Open Sans", Arial, sans-serif;
    position: relative;
  }
  .card {
    position: absolute;
    width: 540px;
    height: 310px;
    border-radius: 18px;
    overflow: hidden;
    background: var(--card-white);
    box-shadow: 0 10px 28px rgba(0,0,0,0.18);
  }
  .card--front { left: 40px; top: 470px; }
  .card--back  { left: 620px; top: 230px; }

  /* front */
  .front-shape { position: absolute; inset: 0; }
  .brand {
    position: absolute;
    left: 34px;
    top: 108px;
    display: flex;
    align-items: center;
    gap: 12px;
  }
  .brand__dot {
    width: 30px; height: 30px;
    border-radius: 50%;
    background: var(--ink-dark);
    flex: none;
  }
  .brand__name {
    font-family: "Cinzel", Georgia, serif;
    font-weight: 500;
    color: var(--ink-dark);
    font-size: 31px;
    letter-spacing: 2px;
    line-height: 1;
  }
  .brand__sub {
    font-family: "Cinzel", Georgia, serif;
    font-weight: 500;
    color: var(--ink-dark);
    font-size: 13px;
    letter-spacing: 2.4px;
    margin-top: 6px;
  }
  .person {
    position: absolute;
    left: 352px;
    top: 40px;
    color: var(--ink-light);
  }
  .person__name { font-weight: 700; font-size: 15px; }
  .person__role { font-style: italic; font-size: 11px; color: var(--ink-muted); margin-top: 2px; }
  .contacts {
    position: absolute;
    left: 322px;
    top: 150px;
    list-style: none;
    color: var(--ink-light);
    font-size: 10px;
  }
  .contacts li {
    display: flex;
    align-items: center;
    gap: 7px;
    height: 21px;
    white-space: nowrap;
  }
  .contacts .icon {
    width: 14px; height: 14px;
    border-radius: 50%;
    background: var(--ink-light);
    display: flex; align-items: center; justify-content: center;
    flex: none;
  }
  .contacts .icon svg { width: 9px; height: 9px; }

  /* back */
  .back-decoration {
    position: absolute;
    left: 170px; top: 30px;
    width: 330px; height: 210px;
    border-radius: 50%;
    background: radial-gradient(ellipse at center, var(--faint-grey) 0%, rgba(220,221,223,0) 70%);
  }
  .back-web {
    position: absolute;
    left: 40px;
    top: 258px;
    font-size: 15px;
    letter-spacing: 3px;
    color: var(--ink-dark);
    white-space: nowrap;
  }
</style>
</head>
<body>

<article class="card card--front">
  <svg class="front-shape" viewBox="0 0 540 310" preserveAspectRatio="none" aria-hidden="true">
    <defs>
      <linearGradient id="panelFill" x1="0" y1="0" x2="0" y2="1">
        <stop offset="0" stop-color="var(--panel-dark)"/>
        <stop offset="1" stop-color="var(--panel-darker)"/>
      </linearGradient>
    </defs>
    <path d="M300 0 C 320 120, 300 220, 220 310 L 212 310 C 292 220, 310 120, 288 0 Z" fill="var(--accent-yellow)"/>
    <path d="M314 0 C 334 120, 316 220, 238 310 L 222 310 C 302 220, 322 120, 300 0 Z" fill="var(--accent-orange)"/>
    <path d="M318 0 C 338 120, 320 220, 242 310 L 540 310 L 540 0 Z" fill="url(#panelFill)"/>
  </svg>

  <div class="brand">
    <span class="brand__dot"></span>
    <div>
      <div class="brand__name">VORNELLE</div>
      <div class="brand__sub">CAPITAL MANAGEMENT</div>
    </div>
  </div>

  <div class="person">
    <div class="person__name">Wanrudee Halvorsen</div>
    <div class="person__role">Chief Operating Officer</div>
  </div>

  <ul class="contacts">
    <li><span class="icon"><svg viewBox="0 0 10 10"><path d="M2 1 L4 1 L4.6 3 L3.4 3.8 Q4.4 5.8 6.2 6.6 L7 5.4 L9 6 L9 8 Q5 9 2 5 Q1 3 2 1 Z" fill="var(--panel-dark)"/></svg></span>+1-555-204-7731</li>
    <li><span class="icon"><svg viewBox="0 0 10 10"><rect x="3" y="1" width="4" height="8" rx="1" fill="var(--panel-dark)"/></svg></span>+1-555-610-2298</li>
    <li><span class="icon"><svg viewBox="0 0 10 10"><rect x="1.5" y="1.5" width="7" height="7" rx="1" fill="var(--panel-dark)"/></svg></span>+1-555-873-4402</li>
    <li><span class="icon"><svg viewBox="0 0 10 10"><rect x="1" y="2.5" width="8" height="5" fill="var(--panel-dark)"/><path d="M1 2.5 L5 5.5 L9 2.5" stroke="var(--ink-light)" stroke-width="0.8" fill="none"/></svg></span>wanru.halvorsen@vornellecap.example</li>
    <li><span class="icon"><svg viewBox="0 0 10 10"><circle cx="5" cy="5" r="3.6" stroke="var(--panel-dark)" stroke-width="1.1" fill="none"/><path d="M1.4 5 H8.6 M5 1.4 V8.6" stroke="var(--panel-dark)" stroke-width="0.8"/></svg></span>www.vornellecap.example</li>
  </ul>
</article>

<article class="card card--back">
  <div class="back-decoration" role="img" aria-label="Faint large brand emblem area"></div>
  <div class="back-web">www.vornellecap.example</div>
</article>

</body>
</html>
```